Flight school sign for building, banner, and bilboard

This sign is primarily for use on the side of our flight school building to draw attention for current and future flight school students. We offer airplane and helicopter flight training, ground school training and seminars, airplane and helicopter rentals, multi-engine training, and more. I would like a professional but exciting sign that can be used across a multitude of signage options such as banners, banner ads, billboard, and other mediums so that our sign is consistent and recognizable.

Contact Information for Business Card

The business card should match our company sign somewhat but not exactly. We want good and exciting imagery or wording and energizing/exciting colors.

```html
<!DOCTYPE html>
<html lang="en">
<head>
<meta charset="utf-8">
<title>Northwind Aviation – Billboard</title>
<link rel="stylesheet" href="https://fonts.googleapis.com/css2?family=Poppins:wght@600;700;800&display=swap">
<style>
  :root {
    --navy: #232a57;
    --navy-deep: #1b2147;
    --red: #e20f14;
    --white: #ffffff;
    --stage: #e4e4e4;
    --sky-top: #6f9fd3;
    --sky-mid: #a9c6e6;
    --runway: #dfe5ec;
    --bar-fade: #3b3b4c;
  }
  * { margin: 0; padding: 0; box-sizing: border-box; }
  html, body {
    width: 1002px;
    height: 1200px;
    overflow: hidden;
    background: var(--stage);
    font-family: "Poppins", sans-serif;
  }
  .billboard {
    position: absolute;
    left: 31px;
    top: 362px;
    width: 940px;
    height: 475px;
    background: var(--navy);
    box-shadow: 0 18px 30px rgba(0, 0, 0, 0.28);
    overflow: hidden;
  }
  .billboard__art {
    position: absolute;
    inset: 0;
    width: 940px;
    height: 475px;
  }
  .brand {
    position: absolute;
    left: 0;
    top: 0;
    width: 318px;
    text-align: center;
    color: var(--white);
  }
  .brand__mark {
    position: absolute;
    left: 134px;
    top: 40px;
    width: 50px;
    height: 50px;
    border: 6px solid var(--white);
    border-radius: 50%;
  }
  .brand__name {
    position: absolute;
    left: 0;
    top: 112px;
    width: 318px;
    font-weight: 700;
    font-size: 22px;
    letter-spacing: 0.5px;
    line-height: 1;
  }
  .brand__tagline {
    position: absolute;
    left: 0;
    top: 141px;
    width: 318px;
    font-weight: 600;
    font-size: 7px;
    letter-spacing: 1px;
    line-height: 1;
  }
  .offer {
    position: absolute;
    left: 33px;
    top: 240px;
    color: var(--navy);
  }
  .offer__title {
    font-weight: 800;
    font-size: 21px;
    line-height: 1;
    margin-bottom: 8px;
  }
  .offer__title em {
    font-style: normal;
    color: var(--red);
  }
  .offer__list { list-style: none; }
  .offer__item {
    position: relative;
    padding-left: 31px;
    font-weight: 700;
    font-size: 15.5px;
    line-height: 19px;
    margin-bottom: 8px;
    text-transform: uppercase;
  }
  .offer__icon {
    position: absolute;
    left: 0;
    top: 1px;
    width: 19px;
    height: 19px;
  }
  .contact-web {
    position: absolute;
    left: 34px;
    top: 415px;
    display: flex;
    align-items: center;
    color: var(--white);
    font-weight: 700;
    font-size: 17px;
    line-height: 1;
  }
  .contact-web__divider {
    width: 1px;
    height: 28px;
    background: var(--white);
    margin: 0 7px;
  }
  .contact-phone {
    position: absolute;
    left: 597px;
    top: 408px;
    display: flex;
    align-items: center;
    gap: 16px;
    color: var(--navy);
    font-weight: 700;
    font-size: 35px;
    line-height: 1;
  }
  .contact-phone__icon { width: 42px; height: 42px; }
</style>
</head>
<body>
  <div class="billboard">
    <svg class="billboard__art" viewBox="0 0 940 475" xmlns="http://www.w3.org/2000/svg">
      <defs>
        <linearGradient id="sky" x1="0" y1="0" x2="0" y2="1">
          <stop offset="0" stop-color="var(--sky-top)"/>
          <stop offset="0.55" stop-color="var(--sky-mid)"/>
          <stop offset="1" stop-color="var(--runway)"/>
        </linearGradient>
        <linearGradient id="barFade" x1="0" y1="0" x2="1" y2="0">
          <stop offset="0.55" stop-color="var(--navy)"/>
          <stop offset="1" stop-color="var(--bar-fade)"/>
        </linearGradient>
      </defs>

      <path class="sweep-red" fill="var(--red)"
        d="M240,0 L258,0 C320,100 420,230 560,300 C680,350 820,330 940,300 L940,378 C800,405 660,400 560,360 C430,300 320,160 240,0 Z"/>
      <path class="hero-photo" fill="url(#sky)" role="img"
        aria-label="Photo of a passenger jet seen head-on on a runway under a blue sky with clouds"
        d="M258,0 L940,0 L940,300 C820,330 680,350 560,300 C420,230 320,100 258,0 Z"/>

      <rect class="phone-strip" x="540" y="405" width="400" height="48" fill="var(--white)"/>

      <path class="offer-panel" fill="var(--white)"
        d="M0,235 C140,195 300,200 420,262 C500,305 545,370 595,475 L0,475 Z"/>
      <path class="offer-arc" fill="var(--red)"
        d="M0,190 C150,150 330,160 450,225 C500,255 535,290 560,330 C540,310 480,280 420,262 C300,200 140,195 0,235 Z"/>

      <polygon class="web-bar" fill="url(#barFade)" points="0,405 566,405 589,453 0,453"/>
    </svg>

    <div class="brand">
      <span class="brand__mark"></span>
      <div class="brand__name">NORTHWIND AVIATION</div>
      <div class="brand__tagline">LEARN TO FLY TODAY, SOAR HIGHER TOMORROW</div>
    </div>

    <div class="offer">
      <h2 class="offer__title">WE <em>OFFER</em></h2>
      <ul class="offer__list">
        <li class="offer__item">
          <svg class="offer__icon" viewBox="0 0 24 24"><path fill="var(--red)" d="M21 16v-2l-8-5V3.5a1.5 1.5 0 0 0-3 0V9l-8 5v2l8-2.5V19l-2 1.5V22l3.5-1 3.5 1v-1.5L13 19v-5.5z" transform="rotate(-45 12 12)"/></svg>
          Airplane and helicopter flight<br>training
        </li>
        <li class="offer__item">
          <svg class="offer__icon" viewBox="0 0 24 24"><path fill="var(--red)" d="M21 16v-2l-8-5V3.5a1.5 1.5 0 0 0-3 0V9l-8 5v2l8-2.5V19l-2 1.5V22l3.5-1 3.5 1v-1.5L13 19v-5.5z" transform="rotate(-45 12 12)"/></svg>
          Ground school training and seminars
        </li>
        <li class="offer__item">
          <svg class="offer__icon" viewBox="0 0 24 24"><path fill="var(--red)" d="M21 16v-2l-8-5V3.5a1.5 1.5 0 0 0-3 0V9l-8 5v2l8-2.5V19l-2 1.5V22l3.5-1 3.5 1v-1.5L13 19v-5.5z" transform="rotate(-45 12 12)"/></svg>
          Airplane and helicopter rentals
        </li>
        <li class="offer__item">
          <svg class="offer__icon" viewBox="0 0 24 24"><path fill="var(--red)" d="M21 16v-2l-8-5V3.5a1.5 1.5 0 0 0-3 0V9l-8 5v2l8-2.5V19l-2 1.5V22l3.5-1 3.5 1v-1.5L13 19v-5.5z" transform="rotate(-45 12 12)"/></svg>
          Multi-engine training and more
        </li>
      </ul>
    </div>

    <div class="contact-web">
      <span class="contact-web__site">www.northwindaviation.com</span>
      <span class="contact-web__divider"></span>
      <span class="contact-web__email">info@northwindaviation.com</span>
    </div>

    <div class="contact-phone">
      <svg class="contact-phone__icon" viewBox="0 0 42 42">
        <circle cx="21" cy="21" r="21" fill="var(--red)"/>
        <circle cx="21" cy="21" r="15" fill="none" stroke="var(--white)" stroke-width="2"/>
        <path fill="var(--white)" d="M15.5 12.5c.8-.5 1.8-.3 2.3.5l1.7 2.8c.4.7.3 1.6-.3 2.1l-1.2 1c.9 2 2.4 3.6 4.4 4.6l1-1.2c.5-.6 1.4-.8 2.1-.4l2.9 1.6c.8.5 1.1 1.5.6 2.3l-1 1.6c-.7 1.1-2 1.6-3.2 1.2-5.2-1.5-9.2-5.5-10.700-10.7-.4-1.2.1-2.5 1.2-3.2z"/>
      </svg>
      <span class="contact-phone__number">(555) 017 2480</span>
    </div>
  </div>
</body>
</html>
```